Compass & Canvas needs new business card design

I need a new business card design. I'm looking for out-of-the-box design which represents the freedom of being a location independent entrepreneur.
I offer coaching, retreats and trips.
I would like to see designs with and without the photo.
Colors I use are black (#000000), green (#25A796) and brown (#D7C38C)
Website compassandcanvas.net

Target Market(s)

location independent entrepreneurs, digital nomads, people looking to swap the 9 to 5 for a lifestyle business

Industry/Entity Type

Business

Contact Information for Business Card

Daria Tolsen
Your Lifestyle Business Coach, Retreat & Trip Leader
http://compassandcanvas.net
hello@compassandcanvas.net
Live a life you don't need a holiday from

Font styles to use
Serif
Sans Serif

Requirements
Must have
• One side should contain only the logo. I would also consider having the "Live a life you don't need a holiday from" on that side too (depending on how it looks)
• Please show both sides on the designs.

```html
<!DOCTYPE html>
<html lang="en">
<head>
<meta charset="utf-8">
<title>Compass &amp; Canvas — Business Card</title>
<link rel="stylesheet" href="https://fonts.googleapis.com/css2?family=Roboto:wght@400;500;700&display=swap">
<style>
  :root {
    --page-bg: #e9e9e7;
    --card-white: #ffffff;
    --card-black: #1f1e1f;
    --ink-dark: #2a2a2a;
    --ink-grey: #5a5a5a;
    --ink-light: #f2f2f2;
    --brand-green: #25a796;
  }
  * { box-sizing: border-box; margin: 0; padding: 0; }
  html, body {
    width: 1200px; height: 950px; overflow: hidden;
    background: var(--page-bg);
    font-family: "Roboto", Arial, sans-serif;
  }
  .sheet {
    width: 1200px; height: 950px;
    display: flex; flex-direction: column; align-items: center; justify-content: center;
    gap: 34px;
  }
  .card {
    position: relative;
    width: 760px; height: 434px;
    border-radius: 4px;
    box-shadow: 0 6px 18px rgba(0,0,0,0.18);
    overflow: hidden;
  }
  /* Front */
  .card--front { background: var(--card-white); color: var(--ink-dark); }
  .wordmark {
    font-family: "Roboto", Arial, sans-serif;
    font-weight: 700;
    text-transform: uppercase;
    letter-spacing: 0.04em;
    line-height: 1;
  }
  .card--front .wordmark {
    position: absolute; right: 64px; top: 78px;
    font-size: 40px; color: var(--ink-dark);
  }
  .holder {
    position: absolute; left: 60px; top: 190px;
  }
  .holder__name {
    font-size: 26px; font-weight: 500; color: var(--brand-green);
    margin-bottom: 10px;
  }
  .holder__role {
    font-size: 19px; color: var(--ink-grey); line-height: 1.35;
  }
  .front-rule {
    position: absolute; left: 60px; right: 60px; top: 318px;
    height: 2px; background: var(--brand-green);
  }
  .contact {
    position: absolute; left: 60px; right: 60px; top: 340px;
    display: flex; gap: 36px;
    font-size: 16px; color: var(--ink-grey);
  }
  .contact__label { color: var(--brand-green); font-weight: 700; }

  /* Back */
  .card--back { background: var(--card-black); color: var(--ink-light); }
  .card--back .wordmark {
    position: absolute; left: 0; right: 0; top: 150px;
    text-align: center; font-size: 52px; color: var(--ink-light);
  }
  .back-rule {
    position: absolute; left: 60px; right: 60px; top: 300px; height: 2px;
    background: linear-gradient(90deg, var(--brand-green), rgba(37,167,150,0));
  }
  .social {
    position: absolute; left: 60px; top: 322px;
    display: flex; gap: 8px;
  }
  .social__square {
    width: 18px; height: 18px; background: var(--brand-green); border-radius: 2px;
  }
  .tagline {
    position: absolute; left: 60px; top: 356px;
    font-size: 17px; letter-spacing: 0.02em; color: var(--ink-light);
  }
</style>
</head>
<body>
<main class="sheet">
  <section class="card card--front" aria-label="Business card front">
    <div class="wordmark">Compass &amp; Canvas</div>
    <div class="holder">
      <p class="holder__name">Daria Tolsen</p>
      <p class="holder__role">Your Lifestyle Business Coach</p>
      <p class="holder__role">Retreat &amp; Trip Leader</p>
    </div>
    <div class="front-rule"></div>
    <div class="contact">
      <span><span class="contact__label">Email</span> : hello@compassandcanvas.net</span>
      <span><span class="contact__label">Web</span> : www.compassandcanvas.net</span>
    </div>
  </section>

  <section class="card card--back" aria-label="Business card back">
    <div class="wordmark">Compass &amp; Canvas</div>
    <div class="back-rule"></div>
    <div class="social" aria-label="Social channels">
      <span class="social__square"></span>
      <span class="social__square"></span>
      <span class="social__square"></span>
    </div>
    <p class="tagline">Live a life you don't need a holiday from</p>
  </section>
</main>
</body>
</html>
```